Wine Label Design Brisden Vale Red Wine

Design for new wine brand "Brisden Vale". Thinking more of an upscale nautical vibe, or something more classic- old school chateau like.
Red Blend or Cabernet
2018 California
Back label copy:
Brisden Vale encapsulates all the wonder of Brisden Beach on a perfect New England summer day. With one sip, you’ll be transported to the pavilions and boardwalks as you get ready to tighten your sails and head out on the Sound. So pull up a chair and pour a glass as you enjoy the warmth of summer in a glass any time you indulge in this wine.

```html
<!DOCTYPE html>
<html lang="en">
<head>
<meta charset="UTF-8">
<title>Brisden Vale Cabernet – Front Label</title>
<link href="https://fonts.googleapis.com/css2?family=Great+Vibes&family=Marcellus&family=Cormorant+Garamond:ital,wght@0,500;1,500&display=swap" rel="stylesheet">
<style>
  :root {
    --page-bg: #ffffff;
    --label-cream: #f4eedc;
    --label-cream-light: #f8f4e6;
    --label-cream-deep: #ece3c8;
    --copper: #b98a72;
    --ink: #2b2a28;
    --ink-soft: #4a4845;
    --sketch-light: #e3ddcb;
    --sketch-mid: #b9b4a6;
    --sketch-dark: #8d897f;
  }
  * { margin: 0; padding: 0; box-sizing: border-box; }
  html, body {
    width: 1200px;
    height: 1200px;
    overflow: hidden;
    background: var(--page-bg);
  }
  .canvas {
    position: relative;
    width: 1200px;
    height: 1200px;
  }
  .label {
    position: absolute;
    left: 220px;
    top: 240px;
    width: 760px;
    height: 720px;
    border-radius: 10px;
    background: linear-gradient(100deg, var(--label-cream-deep) 0%, var(--label-cream-light) 45%, var(--label-cream) 70%, var(--label-cream-deep) 100%);
  }
  .label__frame {
    position: absolute;
    inset: 11px;
    border: 1.5px solid var(--copper);
    border-radius: 12px;
  }
  .label__artwork {
    position: absolute;
    left: 67px;
    top: 96px;
    width: 558px;
    height: 364px;
    border-radius: 6px;
    background: radial-gradient(ellipse at 60% 45%, var(--sketch-mid) 0%, var(--sketch-light) 55%, transparent 80%);
    opacity: 0.85;
  }
  .label__brand {
    position: absolute;
    left: 0;
    right: 0;
    top: 468px;
    text-align: center;
    font-family: "Great Vibes", cursive;
    font-size: 100px;
    line-height: 1;
    color: var(--ink-soft);
  }
  .label__divider {
    position: absolute;
    left: 245px;
    top: 568px;
    width: 270px;
    height: 3px;
  }
  .label__varietal {
    position: absolute;
    left: 0;
    right: 0;
    top: 600px;
    text-align: center;
    font-family: "Marcellus", serif;
    font-size: 36px;
    letter-spacing: 3px;
    color: var(--ink);
  }
  .label__details {
    position: absolute;
    left: 0;
    right: 0;
    top: 668px;
    text-align: center;
    font-family: "Cormorant Garamond", serif;
    font-size: 30px;
    color: var(--ink-soft);
    line-height: 1;
  }
  .label__details .italic { font-style: italic; }
  .label__details .sep { margin: 0 14px; }
</style>
</head>
<body>
  <main class="canvas">
    <section class="label">
      <div class="label__frame"></div>
      <div class="label__artwork" role="img" aria-label="Pen sketch of a lighthouse on a rocky coastal hillside with trees and the sea"></div>
      <h1 class="label__brand">Brisden Vale</h1>
      <svg class="label__divider" viewBox="0 0 270 3" aria-hidden="true">
        <line x1="0" y1="1.5" x2="270" y2="1.5" stroke="#b98a72" stroke-width="1.5"/>
      </svg>
      <p class="label__varietal">CABERNET</p>
      <p class="label__details"><span class="italic">California</span><span class="sep">•</span>2018<span class="sep">•</span><span class="italic">750 ml</span></p>
    </section>
  </main>
</body>
</html>
```